WordPress Website Design for Multi-Brand Aviation Group (Unified Branding System)

Project Overview:
We are seeking a professional, modern WordPress website design for an aviation-focused umbrella company that owns and operates multiple subsidiary businesses. The goal is to create a cohesive visual system that clearly communicates that each company operates under the same parent organization, while still allowing each brand to maintain a slightly distinct identity.
This is not just a single website design—we are looking for a scalable design framework that can be applied across multiple aviation-related businesses.
Objectives:
- Establish a consistent, recognizable brand identity across all company websites
Clearly communicate the relationship between the parent company and its subsidiaries
-bCreate a clean, high-end corporate aviation aesthetic
- Ensure all designs are SEO-friendly and optimized for performance
- Allow flexibility for future expansion (additional subsidiaries)
- Target Audience:
- Corporate aviation clients
- Charter customers
- Students wishing to receive flight training
- Aircraft owners and operators
- Turbine aircraft training to meet insurance requirements
- Business professionals and high-net-worth individuals
- Aviation industry partners
Design Direction & Style:
We are looking for a premium, professional aviation feel—think clean, modern, and high-trust. The design should reflect the standards of corporate aviation: precision, safety, and sophistication.
Key style notes:
Minimalist but impactful layout
High-quality aviation photography (jets, interiors, operations, global travel)
Subtle motion/interaction (hover effects, transitions)
Clear typography hierarchy for readability and professionalism
Branding Requirements:
Incorporate the primary colors of the parent company logo across all designs
Website Structure (Core Pages):
Design a system that includes:
Home Page with the following links:
- About / Company Overview
- Aircraft Management
- Aircraft Acquisition
- Charter
- Pilot Services
- Trip Support
- Contact Page
Site should further include:
- Mobile-first responsive design
- Fast-loading, performance-optimized layouts
SEO & Technical Considerations:
- Design should support high-level SEO implementation:
- Clean layout structure that translates well to semantic HTML
- Proper heading hierarchy (H1, H2, H3)
- Space for keyword-rich content without clutter
- Optimized image placement (with alt text capability)
- Fast load times (lightweight design approach)
- Compatibility with WordPress SEO plugins (e.g., Yoast or Rank Math)
WordPress Requirements:
- Design should be easily built using WordPress (preferred builders: Elementor, Gutenberg, or similar)
- Reusable templates for scalability across multiple sites
- Easy for non-developers to update text and images
- Modular components (blocks/sections that can be reused across pages and sites)
- Navigation & UX:
- Simple, intuitive navigation
- Sticky header preferred
Style guide including:
- Colors
- Fonts
- Button styles
- Layout system
- Designs similar to high-end corporate aviation, private jet charter, or luxury service brands are preferred—clean, sharp, and premium without being overly flashy.
What We Want to Avoid:
- Overly busy layouts
- Generic templates with no brand identity
- Outdated or “stock” looking aviation designs
- Poor mobile responsiveness
Additional Notes:
We are building a long-term brand system, not just a one-off website. There is potential for ongoing work as we expand additional subsidiary sites.
We value designers who understand branding consistency across multiple business units and can create a scalable, professional system.
Include the attached main company logo "Tarnwell Aviation Group" and the "Member FLTC" logo on the main page.
1 page

```html
<!DOCTYPE html>
<html lang="en">
<head>
<meta charset="utf-8">
<title>Tarnwell Aviation Group</title>
<link href="https://fonts.googleapis.com/css2?family=Rajdhani:wght@500;600;700&family=Saira:wght@300;400;500;600&display=swap" rel="stylesheet">
<style>
:root{
  --blue:#0a5bb0;
  --blue-deep:#073f82;
  --navy:#0b1d3a;
  --ink:#111418;
  --night:#05070a;
  --grey-bg:#b4b4b4;
  --muted:#555b63;
  --line:#d9dde3;
  --white:#ffffff;
}
*{box-sizing:border-box;margin:0;padding:0}
html,body{width:1200px;height:2834px;overflow:hidden}
body{background:var(--grey-bg);font-family:"Saira",sans-serif;color:var(--ink)}
.page{position:absolute;left:81px;top:81px;width:1038px;height:2672px;background:var(--white);overflow:hidden;box-shadow:0 6px 18px rgba(0,0,0,.25)}
.abs{position:absolute}
h1,h2,h3,.display{font-family:"Rajdhani",sans-serif;font-weight:700}

/* hero */
.hero-photo{left:0;top:0;width:1038px;height:585px;background:linear-gradient(160deg,#1a2d50 0%,#3f5c86 35%,#c58b55 62%,#27406a 80%,#0d2246 100%)}
.hero-curve{left:0;top:0}
.brand-box{left:0;top:0;width:230px;height:81px;background:var(--white);clip-path:polygon(0 0,100% 0,82% 100%,0 100%)}
.brand-name{left:18px;top:26px;width:180px;font-family:"Rajdhani",sans-serif;font-weight:700;font-size:19px;line-height:18px;color:var(--blue);letter-spacing:.5px}
.nav{left:568px;top:0;width:470px;height:33px;background:var(--white);clip-path:polygon(0 0,100% 0,100% 100%,8% 100%);display:flex;align-items:center;gap:17px;padding-left:50px;font-size:8.5px;font-weight:600;white-space:nowrap}
.nav .active{color:var(--blue);border-bottom:2px solid var(--blue);padding-bottom:3px;margin-top:5px}
.nav .contact{background:var(--blue);color:var(--white);padding:3px 8px;border-radius:10px;font-size:8px}
.eyebrow-band{left:50px;top:148px;width:280px;height:18px;background:var(--blue);clip-path:polygon(0 0,100% 0,95% 100%,0 100%);color:var(--white);font-size:12.5px;letter-spacing:3px;padding-left:33px;line-height:18px;font-weight:500;white-space:nowrap}
.hero-line{left:50px;height:48px;background:#000;color:var(--white);font-size:39px;line-height:48px;padding-left:13px;clip-path:polygon(0 0,100% 0,91% 100%,0 100%);white-space:nowrap}
.hero-copy{left:55px;top:272px;width:310px;border-left:2px solid var(--white);padding-left:5px;color:var(--white);font-size:14px;line-height:21px;font-weight:300}
.btn{display:inline-block;font-family:"Rajdhani",sans-serif;font-weight:700;font-size:11px;color:var(--white);height:22px;line-height:22px;padding:0 22px;white-space:nowrap}
.btn-blue{background:var(--blue);clip-path:polygon(6% 0,100% 0,94% 100%,0 100%)}
.btn-dark{background:#000;clip-path:polygon(6% 0,100% 0,94% 100%,0 100%)}
.member{left:710px;top:466px;width:280px;text-align:center}
.member small{display:block;font-size:9px;color:var(--ink)}
.member-name{display:inline-flex;align-items:center;gap:8px;font-family:"Rajdhani",sans-serif;font-weight:700;font-size:26px;color:var(--navy);letter-spacing:3px;line-height:26px}
.member-name i{width:36px;height:22px;border-radius:50%;background:var(--blue)}
.member .strong{font-size:9.5px;font-weight:600;margin-top:4px}
.member .sub{font-size:8.5px;color:var(--muted)}

/* section labels */
.label{display:flex;align-items:center;justify-content:center}
.label span.rule{flex:none;width:64px;height:2px;background:var(--ink)}
.label b{flex:none;white-space:nowrap;background:var(--blue);color:var(--white);font-family:"Saira",sans-serif;font-weight:500;font-size:12.5px;letter-spacing:3px;padding:0 24px;height:20px;line-height:20px;clip-path:polygon(0 0,100% 0,88% 100%,12% 100%)}

/* who */
.who-label{left:51px;top:682px;width:300px;justify-content:flex-start}
.who h2{left:51px;top:712px;font-size:37px;line-height:42px;color:var(--ink)}
.who p{left:51px;top:803px;width:460px;font-size:8.3px;line-height:14px;color:var(--ink)}
.who .btn{left:51px;top:874px;height:17px;line-height:17px;font-size:9px;padding:0 18px}
.who-photo{left:514px;top:653px;width:471px;height:266px;background:linear-gradient(120deg,#2a2420,#7b6c5c 45%,#e9e4dc 70%,#4f463d);clip-path:polygon(13% 0,100% 0,86% 100%,0 100%)}
.tri-a{left:541px;top:653px;width:85px;height:100px;background:var(--blue);clip-path:polygon(0 0,100% 0,55% 100%)}
.tri-b{left:880px;top:823px;width:85px;height:96px;background:var(--blue);clip-path:polygon(50% 0,100% 100%,0 100%)}

/* services */
.svc-bg{left:0;top:990px;width:1038px;height:580px;background:linear-gradient(180deg,#f4f6f9,#e6ebf1);clip-path:polygon(0 22%,62% 0,100% 10%,100% 100%,0 100%)}
.svc-label{left:0;top:1065px;width:1038px}
.svc h2{left:0;top:1095px;width:1038px;text-align:center;font-size:35px;letter-spacing:.5px}
.svc .lede{left:0;top:1141px;width:1038px;text-align:center;font-size:14px;line-height:20px;color:#333;font-weight:300}
.card{width:297px;height:170px;background:var(--white);box-shadow:0 2px 8px rgba(0,0,0,.08);padding:26px 22px 0 26px}
.card .head{display:flex;align-items:center;gap:12px;height:58px}
.card .ico{width:58px;height:58px;border-radius:50%;background:var(--blue);flex:none;display:flex;align-items:center;justify-content:center}
.card h3{font-size:18px;line-height:21px}
.card p{font-size:7.6px;line-height:14px;margin-top:17px;color:#333}
.card a{display:block;margin-top:6px;font-size:9px;font-weight:600;color:var(--blue);text-decoration:none}
.card a:after{content:"";display:inline-block;width:26px;height:1px;background:var(--blue);margin-left:6px;vertical-align:middle}
.card.feature{background:linear-gradient(135deg,#1b5fae,#0a4c99 60%,#0d3f7f)}
.card.feature h3,.card.feature p,.card.feature a{color:var(--white)}
.card.feature a:after{background:var(--white)}
.card.feature .ico{background:var(--white)}

/* pillars */
.pillars{left:51px;top:1662px;width:936px;height:50px;display:flex}
.pillar{flex:1;display:flex;align-items:center;gap:10px;border-right:1px solid var(--line)}
.pillar:nth-child(n+2){padding-left:50px}
.pillar:last-child{border-right:none}
.pillar svg{flex:none}
.pillar b{display:block;font-family:"Rajdhani",sans-serif;font-weight:700;font-size:15px;line-height:16px}
.pillar span{font-size:11.5px;color:#333;font-weight:300}

/* fleet */
.fleet-bg{left:0;top:1756px;width:1038px;height:396px;background:var(--night);clip-path:polygon(0 0,25% 7%,50% 8%,75% 7%,100% 0,100% 100%,0 100%)}
.fleet-photo{left:230px;top:1742px;width:578px;height:150px;border-radius:6px;background:linear-gradient(180deg,#2a2f36 0%,#1a1e24 100%)}
.fleet-label{left:0;top:1928px;width:1038px}
.fleet-label span.rule{background:var(--white)}
.fleet h2{left:0;top:1958px;width:1038px;text-align:center;color:var(--white);font-size:36px}
.fleet p{left:0;top:2006px;width:1038px;text-align:center;color:var(--white);font-size:12.5px;line-height:22px;font-weight:300}
.fleet .btn{left:388px;top:2068px;height:28px;line-height:28px;font-size:12px;padding:0 32px}

/* cta */
.cta-bg{left:0;top:2152px;width:1038px;height:222px;background:linear-gradient(100deg,#0b55a8,#0a5bb0 55%,#2a6fb9)}
.cta h2{left:0;top:2196px;width:1038px;text-align:center;color:var(--white);font-size:35px}
.cta p{left:0;top:2242px;width:1038px;text-align:center;color:var(--white);font-size:14px;line-height:22px;font-weight:300}
.cta .btn{left:425px;top:2300px;background:var(--white);color:var(--blue);height:28px;line-height:28px;font-size:12px;padding:0 34px;clip-path:polygon(8% 0,100% 0,92% 100%,0 100%)}

/* footer */
.foot-brand{left:138px;top:2440px;width:180px;font-family:"Rajdhani",sans-serif;font-weight:700;font-size:21px;line-height:20px;color:var(--blue)}
.foot-about{left:138px;top:2491px;width:170px;font-size:8.5px;line-height:13px;color:#222}
.foot-member{left:138px;top:2549px;text-align:left}
.foot-member small{display:block;font-size:9px;padding-left:46px}
.vline{width:1px;height:180px;background:var(--line);top:2414px}
.col h4{font-family:"Rajdhani",sans-serif;font-weight:700;font-size:13px;color:var(--blue);margin-bottom:8px}
.col li{list-style:none;font-size:8.5px;line-height:19.3px;color:#222;white-space:nowrap}
.col li:before{content:"";display:inline-block;border-left:5px solid var(--blue);border-top:3px solid transparent;border-bottom:3px solid transparent;margin-right:5px}
.col.contact li:before{display:none}
.col.contact li{display:flex;align-items:flex-start;gap:6px;line-height:12px;margin-bottom:10px}
.foot-rule{left:138px;top:2623px;width:762px;height:1px;background:var(--line)}
.copy{left:138px;top:2639px;font-size:8.5px;color:#222}
.legal{left:763px;top:2639px;font-size:8.5px;color:#222;display:flex;gap:20px}
</style>
</head>
<body>
<div class="page">

  <header class="hero">
    <div class="abs hero-photo" role="img" aria-label="Private business jet parked on a wet apron at sunset"></div>
    <svg class="abs hero-curve" width="1038" height="600" viewBox="0 0 1038 600" aria-hidden="true">
      <path d="M0 475 C120 530 260 565 420 585 C600 520 820 420 1038 325 L1038 600 L0 600 Z" fill="#fff"/>
    </svg>
    <div class="abs brand-box"></div>
    <div class="abs brand-name">TARNWELL<br>AVIATION GROUP</div>
    <nav class="abs nav">
      <span class="active">Home</span><span>About</span><span>Aircraft Management</span><span>Charter</span><span>Pilot Services</span><span>Trip Support</span><span class="contact">CONTACT</span>
    </nav>
    <div class="abs eyebrow-band">TARNWELL AVIATION GROUP</div>
    <h1>
      <span class="abs hero-line" style="top:168px;width:387px">ELEVATING AVIATION</span>
      <span class="abs hero-line" style="top:221px;width:247px">EXCELLENCE</span>
    </h1>
    <p class="abs hero-copy">A unified aviation group delivering world-class aircraft management, charter, acquisition, and pilot services with precision, safety, and trust.</p>
    <div class="abs" style="left:51px;top:356px;display:flex;gap:40px">
      <a class="btn btn-blue">START A CONSULTATION</a>
      <a class="btn btn-dark">EXPLORE SERVICES</a>
    </div>
    <div class="abs member">
      <small>member of</small>
      <span class="member-name"><i></i>FLTC</span>
      <div class="strong">Built for operators, owners, and charter clients.</div>
      <div class="sub">Precision-led service architecture for every aviation business unit.</div>
    </div>
  </header>

  <section class="who">
    <div class="abs label who-label"><span class="rule"></span><b>WHO WE ARE</b><span class="rule"></span></div>
    <h2 class="abs">A Unified Approach to<br>Aviation Services</h2>
    <p class="abs">Tarnwell Aviation Group brings together multiple aviation-focused businesses under one trusted brand. We provide seamless, high-quality services across aircraft management, charter, acquisition, and training. Our team works with corporate clients, aircraft owners, and aviation professionals, delivering consistent excellence while allowing each specialized division to operate with focused expertise.</p>
    <a class="abs btn btn-blue">LEARN MORE &rarr;</a>
    <div class="abs who-photo" role="img" aria-label="Pilot reading a chart in a private jet cabin"></div>
    <div class="abs tri-a"></div>
    <div class="abs tri-b"></div>
  </section>

  <section class="svc">
    <div class="abs svc-bg" role="img" aria-label="Faded hangar interior backdrop"></div>
    <div class="abs label svc-label"><span class="rule"></span><b>WHAT WE DO</b><span class="rule"></span></div>
    <h2 class="abs">COMPREHENSIVE AVIATION SOLUTIONS</h2>
    <p class="abs lede">Our integrated service offering ensures that every aspect of aviation is handled<br>with precision, efficiency, and professionalism.</p>

    <article class="abs card" style="left:51px;top:1208px">
      <div class="head"><span class="ico"><svg width="28" height="28" viewBox="0 0 28 28" fill="none" stroke="#fff" stroke-width="1.6"><circle cx="14" cy="14" r="9"/><circle cx="14" cy="14" r="3.5"/></svg></span><h3>Aircraft<br>Management</h3></div>
      <p>End-to-end aircraft management solutions designed to optimize performance, ensure compliance, and deliver peace of mind.</p>
      <a>Learn More</a>
    </article>
    <article class="abs card" style="left:370px;top:1208px">
      <div class="head"><span class="ico"><svg width="28" height="28" viewBox="0 0 28 28" fill="none" stroke="#fff" stroke-width="1.6"><rect x="4" y="5" width="20" height="12" rx="2"/><path d="M6 22h16"/></svg></span><h3>Aircraft<br>Acquisition</h3></div>
      <p>Expert guidance through buying and selling aircraft, backed by market insight and industry experience to secure the best value.</p>
      <a>View Details</a>
    </article>
    <article class="abs card" style="left:689px;top:1208px">
      <div class="head"><span class="ico"><svg width="28" height="28" viewBox="0 0 28 28" fill="none" stroke="#fff" stroke-width="1.6"><path d="M4 16l20-7-5 11-4-4-5 3z"/></svg></span><h3>Charter<br>Services</h3></div>
      <p>On-demand charter services offering flexibility, comfort, and efficiency—tailored to your schedule and travel requirements.</p>
      <a>Book a Flight</a>
    </article>
    <article class="abs card" style="left:51px;top:1396px">
      <div class="head"><span class="ico"><svg width="28" height="28" viewBox="0 0 28 28" fill="none" stroke="#fff" stroke-width="1.6"><circle cx="14" cy="10" r="4"/><path d="M6 23c1-5 5-7 8-7s7 2 8 7"/></svg></span><h3>Global<br>Trip Support</h3></div>
      <p>Comprehensive trip planning including permits, fuel coordination, and ground logistics to ensure seamless operations worldwide.</p>
      <a>Find pilot support</a>
    </article>
    <article class="abs card" style="left:370px;top:1396px">
      <div class="head"><span class="ico"><svg width="28" height="28" viewBox="0 0 28 28" fill="none" stroke="#fff" stroke-width="1.6"><circle cx="14" cy="14" r="9"/><path d="M5 14h18M14 5c3 3 3 15 0 18M14 5c-3 3-3 15 0 18"/></svg></span><h3>Global Trip<br>Support</h3></div>
      <p>Mission planning, coordination, logistics, and responsive operational support from departure to arrival.</p>
      <a>Get Support</a>
    </article>
    <article class="abs card feature" style="left:689px;top:1396px" role="img" aria-label="Pilots in a training session over a blue overlay">
      <div class="head"><span class="ico"><svg width="28" height="28" viewBox="0 0 28 28" fill="none" stroke="#0a5bb0" stroke-width="1.6"><rect x="5" y="5" width="18" height="12" rx="1"/><circle cx="9" cy="21" r="2"/><circle cx="19" cy="21" r="2"/></svg></span><h3>Turbine Training<br>Programs</h3></div>
      <p>Advanced pilot training programs designed to meet insurance requirements and enhance operational safety and performance.</p>
      <a>Start Training</a>
    </article>
  </section>

  <section class="abs pillars">
    <div class="pillar"><svg width="36" height="36" viewBox="0 0 36 36" fill="none" stroke="#0a5bb0" stroke-width="1.8"><path d="M18 4l12 5v8c0 8-6 13-12 15C12 30 6 25 6 17V9z"/><path d="M12 18l4 4 8-8"/></svg><div><b>SAFETY</b><span>Our Highest Standard</span></div></div>
    <div class="pillar"><svg width="36" height="36" viewBox="0 0 36 36" fill="none" stroke="#0a5bb0" stroke-width="1.8"><circle cx="18" cy="18" r="11"/><path d="M7 18h22M18 7c4 4 4 18 0 22M18 7c-4 4-4 18 0 22"/></svg><div><b>GLOBAL REACH</b><span>Worldwide Solutions</span></div></div>
    <div class="pillar"><svg width="36" height="36" viewBox="0 0 36 36" fill="none" stroke="#0a5bb0" stroke-width="1.8"><path d="M5 11V5h6M25 5h6v6M31 25v6h-6M11 31H5v-6"/><circle cx="18" cy="15" r="4"/><path d="M10 27c1-5 5-7 8-7s7 2 8 7"/></svg><div><b>CLIENT FOCUSED</b><span>Personalized Service</span></div></div>
    <div class="pillar"><svg width="36" height="36" viewBox="0 0 36 36" fill="none" stroke="#0a5bb0" stroke-width="1.8"><circle cx="18" cy="16" r="10"/><path d="M13 25l-3 8 8-3 8 3-3-8"/></svg><div><b>EXCELLENCE</b><span>In Every Detail</span></div></div>
  </section>

  <section class="fleet">
    <div class="abs fleet-bg"></div>
    <div class="abs fleet-photo" role="img" aria-label="Front view of a white airliner in flight"></div>
    <div class="abs label fleet-label"><span class="rule"></span><b>OUR FLEET</b><span class="rule"></span></div>
    <h2 class="abs">Access the Right Aircraft for Every Mission</h2>
    <p class="abs">From light jets to long-range aircraft, we provide access to a diverse fleet that meets the highest standards<br>of performance, comfort and reliability.</p>
    <a class="abs btn btn-blue">VIEW AIRCRAFT OPTIONS</a>
  </section>

  <section class="cta">
    <div class="abs cta-bg" role="img" aria-label="Blue-toned aviation backdrop"></div>
    <h2 class="abs">Ready to Elevate Your Aviation Experience?</h2>
    <p class="abs">Contact our team today to discuss how we can support your<br>aviation needs.</p>
    <a class="abs btn">GET IN TOUCH</a>
  </section>

  <footer>
    <div class="abs foot-brand">TARNWELL<br>AVIATION GROUP</div>
    <p class="abs foot-about">Delivering world-class aviation solutions through a family of trusted companies committed to safety, service, and sophistication.</p>
    <div class="abs foot-member"><small>member of</small><span class="member-name"><i></i>FLTC</span></div>
    <div class="abs vline" style="left:365px"></div>
    <div class="abs vline" style="left:712px"></div>
    <div class="abs col" style="left:415px;top:2430px"><h4>QUICK LINKS</h4><ul><li>About</li><li>Aircraft Management</li><li>Aircraft Acquisition</li><li>Charter</li><li>Pilot Services</li><li>Trip Support</li><li>Contact</li></ul></div>
    <div class="abs col" style="left:571px;top:2430px"><h4>SERVICES</h4><ul><li>Aircraft Management</li><li>Aircraft Acquisition</li><li>Charter</li><li>Pilot Services</li><li>Trip Support</li></ul></div>
    <div class="abs col contact" style="left:761px;top:2430px"><h4>CONTACT INFO</h4><ul>
      <li><svg width="11" height="11" viewBox="0 0 12 12" fill="none" stroke="#0a5bb0" stroke-width="1.3"><path d="M3 1h2l1 3-1.5 1a7 7 0 003 3L9 6.5l3 1v2c0 1-1 2-2 2C5 11 1 7 1 2c0-.5.5-1 2-1z"/></svg>+1 (555) 014-2290</li>
      <li><svg width="11" height="11" viewBox="0 0 12 12" fill="none" stroke="#0a5bb0" stroke-width="1.3"><rect x="1" y="2.5" width="10" height="7"/><path d="M1 3l5 4 5-4"/></svg>info@tarnwellaviationgroup.com</li>
      <li><svg width="11" height="11" viewBox="0 0 12 12" fill="none" stroke="#0a5bb0" stroke-width="1.3"><path d="M6 11S2 7 2 4.5a4 4 0 018 0C10 7 6 11 6 11z"/><circle cx="6" cy="4.5" r="1.3"/></svg><span>48 Hangar Row, Suite 210<br>Opa Creek, FL 33190, USA</span></li>
      <li><svg width="11" height="11" viewBox="0 0 12 12" fill="none" stroke="#0a5bb0" stroke-width="1.3"><rect x="1" y="2" width="10" height="8"/><path d="M3 5h3M3 7h5"/></svg>24/7 Support Available</li>
    </ul></div>
    <div class="abs foot-rule"></div>
    <div class="abs copy">© 2024 Tarnwell Aviation Group. All rights reserved.</div>
    <div class="abs legal"><span>Privacy Policy</span><span>Terms of Service</span></div>
  </footer>

</div>
</body>
</html>
```